Creative packaging for Scandinavian Coffee brand

Kvå is a new-to-the-world Scandinavian coffee brand, offering a top-quality instant coffee product laden with health benefits. The ‘coffee moment’ is a sacred part of life in Scandinavia: it represents a pause from the day – a peaceful, quiet break in which you detach, sit back and just focus on being present for a while. The success of Kvå will be built on two critical drivers: 1) a delicious product, and 2) a modern “love brand”, which young consumers will identify with and be proud to display on their shelves.
We want Kvå packaging design and branding to be a visually stunning representation of our brand values of savour, sustainability and authenticity – and convey a strong link back to our Scandinavian heritage.
The packaging we are looking for should be:
Product: 500ml container of instant coffee
Packaging design (3D): we welcome unusual shapes/materials to help us stand out at shelf and convey a premium/modern look & feel. However, the pack should still be a) practical for shipping (i.e. not too fragile or complicated to pack in large quantities) and b) sustainable.
Artwork (2D): should look modern/sophisticated/minimalist (think: Scandinavian design) – but ideally with a unique twist that helps it stand out at shelf. Preferred dominant colours are whites or blacks. Artwork must include the logo (attached, can be either black on white or white on black).
Optional: we will also be selling single-serve packets to go with the 500ml packet, which could be sold either in sachets, capsules or other interesting packaging, with a consistent look & feel as the main packet.
We hope to stand out in a crowded category – so please feel free to stretch your imagination beyond what is currently available on shelf! (we've attached an example of a typical instant coffee shelf for perspective)
Target Market(s)
Millennial / young consumers, who are willing to spend a little extra for an appealing design

```html
<!DOCTYPE html>
<html lang="en">
<head>
<meta charset="UTF-8">
<title>Kvå Scandinavian Coffee — Label Artwork</title>
<link rel="stylesheet" href="https://fonts.googleapis.com/css2?family=Josefin+Sans:wght@300&display=swap">
<style>
  :root {
    --ink: #0b0b0b;
    --ink-soft: #1c1c1c;
    --charcoal: #333333;
    --charcoal-deep: #2a2a2a;
    --paper: #ffffff;
    --mist: #ececec;
    --bevel: #9a9a9a;
    --divider: #000000;
  }
  html, body {
    margin: 0;
    padding: 0;
    width: 862px;
    height: 1200px;
    overflow: hidden;
    background: var(--paper);
  }
  .canvas {
    position: relative;
    width: 862px;
    height: 1200px;
    display: flex;
    font-family: "Josefin Sans", sans-serif;
  }
  .label {
    position: relative;
    width: 430px;
    height: 1200px;
    overflow: hidden;
  }
  .label svg {
    position: absolute;
    inset: 0;
    width: 430px;
    height: 1200px;
  }
  .divider {
    width: 2px;
    height: 1200px;
    background: var(--divider);
  }
  .brand-lockup {
    position: absolute;
    left: 0;
    right: 0;
    top: 528px;
    text-align: center;
    -webkit-font-smoothing: antialiased;
  }
  .brand-name {
    margin: 0;
    font-weight: 300;
    font-size: 108px;
    line-height: 1;
    letter-spacing: 10px;
    padding-left: 10px;
  }
  .brand-tagline {
    margin: 12px 0 0;
    font-weight: 300;
    font-size: 13px;
    letter-spacing: 4px;
    padding-left: 4px;
  }
  .label--dark .brand-name,
  .label--dark .brand-tagline { color: var(--paper); }
  .label--light .brand-name,
  .label--light .brand-tagline { color: var(--ink); }
</style>
</head>
<body>
<main class="canvas">
  <section class="label label--dark">
    <svg viewBox="0 0 430 1200">
      <defs>
        <linearGradient id="ridgeShadeDark" x1="0" y1="0" x2="1" y2="0">
          <stop offset="0" stop-color="#0b0b0b"/>
          <stop offset="0.18" stop-color="#1e1e1e"/>
          <stop offset="0.3" stop-color="#0b0b0b"/>
          <stop offset="0.55" stop-color="#202020"/>
          <stop offset="0.68" stop-color="#0b0b0b"/>
          <stop offset="0.88" stop-color="#1c1c1c"/>
          <stop offset="1" stop-color="#0b0b0b"/>
        </linearGradient>
        <linearGradient id="bandShade" x1="0" y1="0" x2="0" y2="1">
          <stop offset="0" stop-color="#2a2a2a"/>
          <stop offset="0.5" stop-color="#363636"/>
          <stop offset="1" stop-color="#2c2c2c"/>
        </linearGradient>
        <linearGradient id="drift" x1="0" y1="0" x2="1" y2="1">
          <stop offset="0" stop-color="#ffffff"/>
          <stop offset="0.5" stop-color="#f6f6f6"/>
          <stop offset="1" stop-color="#ececec"/>
        </linearGradient>
        <filter id="liftDark" x="-10%" y="-10%" width="120%" height="130%">
          <feDropShadow dx="0" dy="6" stdDeviation="5" flood-color="#000" flood-opacity="0.55"/>
        </filter>
      </defs>
      <rect x="0" y="0" width="430" height="1200" fill="url(#bandShade)"/>
      <path role="img" aria-label="Black band of flowing white contour lines, like snowy mountain ridges"
        fill="url(#ridgeShadeDark)" filter="url(#liftDark)"
        d="M0,0 H430 V400 C400,395 390,440 350,430 C320,422 300,445 260,440 C230,436 215,460 180,452 C140,444 120,470 80,458 C50,450 25,470 0,462 Z"/>
      <path fill="none" stroke="var(--bevel)" stroke-width="2" opacity="0.8"
        d="M430,403 C400,398 390,443 350,433 C320,425 300,448 260,443 C230,439 215,463 180,455 C140,447 120,473 80,461 C50,453 25,473 0,465"/>
      <path role="img" aria-label="White field of flowing black contour lines, like snowdrifts"
        fill="url(#drift)" filter="url(#liftDark)"
        d="M0,800 C30,790 50,770 80,780 C110,790 130,760 160,765 C200,772 220,745 260,752 C300,758 320,735 350,745 C380,755 400,740 430,748 V1210 H0 Z"/>
    </svg>
    <div class="brand-lockup">
      <p class="brand-name">KVÅ</p>
      <p class="brand-tagline">SCANDINAVIAN COFFEE</p>
    </div>
  </section>

  <div class="divider"></div>

  <section class="label label--light">
    <svg viewBox="0 0 430 1200">
      <defs>
        <linearGradient id="ridgeShadeLight" x1="0" y1="0" x2="1" y2="0">
          <stop offset="0" stop-color="#0b0b0b"/>
          <stop offset="0.2" stop-color="#1d1d1d"/>
          <stop offset="0.35" stop-color="#0b0b0b"/>
          <stop offset="0.6" stop-color="#1f1f1f"/>
          <stop offset="0.75" stop-color="#0b0b0b"/>
          <stop offset="0.9" stop-color="#1b1b1b"/>
          <stop offset="1" stop-color="#0b0b0b"/>
        </linearGradient>
        <linearGradient id="mistFade" x1="0" y1="0" x2="0" y2="1">
          <stop offset="0" stop-color="#ffffff"/>
          <stop offset="0.4" stop-color="#f7f7f7"/>
          <stop offset="1" stop-color="#ececec"/>
        </linearGradient>
        <filter id="liftLight" x="-10%" y="-10%" width="120%" height="130%">
          <feDropShadow dx="0" dy="5" stdDeviation="5" flood-color="#000" flood-opacity="0.3"/>
        </filter>
      </defs>
      <rect x="0" y="0" width="430" height="1200" fill="var(--paper)"/>
      <path role="img" aria-label="Black band of flowing white contour lines, like snowy mountain ridges"
        fill="url(#ridgeShadeLight)" filter="url(#liftLight)"
        d="M0,0 H430 V400 C400,395 390,440 350,430 C320,422 300,445 260,440 C230,436 215,460 180,452 C140,444 120,470 80,458 C50,450 25,470 0,462 Z"/>
      <path role="img" aria-label="White field of fine black contour lines, like snowdrifts"
        fill="url(#mistFade)" stroke="var(--ink)" stroke-width="1" filter="url(#liftLight)"
        d="M-2,800 C30,790 50,770 80,780 C110,790 130,760 160,765 C200,772 220,745 260,752 C300,758 320,735 350,745 C380,755 400,740 432,748 V1210 H-2 Z"/>
    </svg>
    <div class="brand-lockup">
      <p class="brand-name">KVÅ</p>
      <p class="brand-tagline">SCANDINAVIAN COFFEE</p>
    </div>
  </section>
</main>
</body>
</html>
```